3D sculpture business needs a website

We have created a cool new way to make customized/personalized sculptures.

We scan you from head to toe, digitize you, and print you into your very own sculpture, charm, pendent, or anything else you can imagine.

We are looking for a starter website, an introduction to the products and service including photos, descriptive text, and contact info. A contact/about page, a blog page and events page.

All pages can be hard coded for content, no database required for this version.

Industry/Entity Type

Events

Requirements
Must have
• HTML5
JQuery
Mobile formatting
Nice to have
• Visual Studio Solution
ASP.Net MVC4
Hosted on Windows Azure

```html
<!DOCTYPE html>
<html lang="en">
<head>
<meta charset="utf-8">
<title>Contact Us – TinyTwinWorks</title>
<link rel="stylesheet" href="https://fonts.googleapis.com/css2?family=Arimo:wght@400;700&display=swap">
<style>
  :root {
    --page-black: #000000;
    --accent-cyan: #1fe4f0;
    --brand-blue: #2f80f6;
    --nav-white: #ffffff;
    --required-red: #ff2020;
    --hint-grey: #9a9a9a;
    --field-white: #ffffff;
    --field-border: #bdbdbd;
    --rule-grey: #cfcfcf;
    --bg-teal: #0a5f80;
    --bg-deep: #06202e;
    --bg-violet: #8a3aa8;
    --bg-wine: #6a1230;
  }
  * { box-sizing: border-box; margin: 0; padding: 0; }
  html, body { width: 1200px; height: 820px; overflow: hidden; }
  body {
    position: relative;
    font-family: "Arimo", Arial, sans-serif;
    background:
      radial-gradient(circle at 90% 40%, rgba(200,120,220,0.45), transparent 28%),
      radial-gradient(circle at 8% 60%, rgba(40,150,190,0.35), transparent 25%),
      linear-gradient(90deg, var(--bg-deep) 0%, var(--bg-teal) 24%, #3b5ca8 45%, var(--bg-violet) 68%, #9a2a78 86%, var(--bg-wine) 100%);
  }
  .page-panel {
    position: absolute; left: 310px; top: 8px;
    width: 580px; height: 812px;
    background: var(--page-black);
  }
  .site-nav {
    position: absolute; left: 475px; top: 25px;
    font-size: 18px; color: var(--nav-white); white-space: nowrap;
  }
  .site-nav a { color: var(--nav-white); text-decoration: none; }
  .site-nav a.is-current { color: var(--accent-cyan); }
  .site-nav .divider { margin: 0 4px; }
  .brand-figure {
    position: absolute; left: 346px; top: 22px; width: 84px; height: 188px;
    border-radius: 30px 30px 10px 10px;
    background: linear-gradient(160deg, #d9d9d9, #6d6d6d 55%, #2a2a2a);
  }
  .brand-name {
    position: absolute; left: 443px; top: 90px;
    font-size: 46px; font-weight: 700; color: var(--brand-blue);
    letter-spacing: -0.5px; white-space: nowrap;
  }
  .brand-tagline {
    position: absolute; left: 446px; top: 176px;
    font-size: 24px; font-weight: 400; color: var(--nav-white);
    letter-spacing: 1.5px; white-space: nowrap;
  }
  .contact-title {
    position: absolute; left: 348px; top: 248px;
    font-size: 23px; font-weight: 700; color: var(--accent-cyan);
  }
  .contact-intro {
    position: absolute; left: 348px; top: 281px;
    font-size: 14px; color: var(--accent-cyan);
  }
  .section-rule {
    position: absolute; left: 348px; top: 323px; width: 502px;
    border: 0; border-top: 1px solid var(--rule-grey);
  }
  .field-label {
    position: absolute; left: 348px;
    font-size: 13px; font-weight: 700; color: var(--accent-cyan);
  }
  .field-label .required { color: var(--required-red); margin-left: 3px; }
  .text-field {
    position: absolute; background: var(--field-white);
    border: 1px solid var(--field-border);
    font-family: inherit; font-size: 14px; padding: 3px 5px; color: #888;
  }
  .text-field::placeholder { color: #a8a8a8; }
  .sub-label {
    position: absolute; font-size: 10px; color: var(--hint-grey);
  }
  .phone-dash {
    position: absolute; left: 410px; top: 563px; color: var(--hint-grey); font-size: 13px;
  }
  .captcha-box {
    position: absolute; left: 348px; top: 761px; width: 161px; height: 70px;
    background: #f1f1f1; border: 1px solid #cfcfcf; border-radius: 4px;
  }
  .captcha-image {
    position: absolute; left: 364px; top: 773px; width: 136px; height: 30px;
    background: linear-gradient(90deg, #e9ecec, #d8dcdc);
    border: 1px solid #bbbbbb;
  }
  .captcha-answer {
    position: absolute; left: 356px; top: 812px; width: 140px; height: 20px;
    background: var(--field-white); border: 1px solid #c4c4c4;
  }
</style>
</head>
<body>
  <div class="page-panel"></div>

  <nav class="site-nav">
    <a href="#">about us</a><span class="divider">|</span><a href="#" class="is-current">contact</a><span class="divider">|</span><a href="#">blog</a><span class="divider">|</span><a href="#">events</a>
  </nav>

  <div class="brand-figure" role="img" aria-label="Photo of a small silver sculpture of a posing figure"></div>
  <div class="brand-name">TinyTwinWorks.com</div>
  <div class="brand-tagline">making lasting memories</div>

  <h1 class="contact-title">Contact Us!</h1>
  <p class="contact-intro">Contact us now to get started creating your own Tiny Twin!</p>
  <hr class="section-rule">

  <label class="field-label" style="top:354px">Your Name<span class="required">*</span></label>
  <input class="text-field" style="left:349px;top:380px;width:97px;height:23px">
  <input class="text-field" style="left:455px;top:380px;width:125px;height:23px">
  <span class="sub-label" style="left:349px;top:410px">First Name</span>
  <span class="sub-label" style="left:453px;top:410px">Last Name</span>

  <label class="field-label" style="top:451px">Your E-mail Address<span class="required">*</span></label>
  <input class="text-field" style="left:349px;top:476px;width:225px;height:24px" placeholder="ex: myname@example.com">

  <label class="field-label" style="top:532px">Phone Number</label>
  <input class="text-field" style="left:349px;top:557px;width:57px;height:24px">
  <span class="phone-dash">-</span>
  <input class="text-field" style="left:422px;top:557px;width:86px;height:24px">
  <span class="sub-label" style="left:349px;top:587px">Area Code</span>
  <span class="sub-label" style="left:421px;top:587px">Phone Number</span>

  <label class="field-label" style="top:628px">Your Message<span class="required">*</span></label>
  <textarea class="text-field" style="left:349px;top:654px;width:223px;height:48px;resize:both"></textarea>

  <label class="field-label" style="top:737px">Enter the message as it's shown<span class="required">*</span></label>
  <div class="captcha-box"></div>
  <div class="captcha-image" role="img" aria-label="Distorted verification word"></div>
  <div class="captcha-answer"></div>
</body>
</html>
```